VELMIRAN (coffee package design)

Make coffee bag for coffee beans: VELMIRAN is a quality-driven coffee roaster focused on crafting fresh, flavorful coffee from premium beans sourced directly from farms. We build close relationships with growers to ensure ethical practices, traceability, and exceptional quality at the origin. Our small-batch roasting approach brings out the unique character of each bean—highlighting bold notes, rich complexity, and peak freshness. At VELMIRAN, we believe great coffee starts at the source—and ends in your cup, roasted to perfection.

**VELMIRAN** is a quality-driven coffee roaster focused on crafting fresh, flavorful coffee from **premium beans sourced directly from farms**. We build close relationships with growers to ensure ethical practices, traceability, and exceptional quality at the origin. Our small-batch roasting approach brings out the unique character of each bean—highlighting bold notes, rich complexity, and peak freshness. At **VELMIRAN**, we believe great coffee starts at the source—and ends in your cup, roasted to perfection.

VELMIRAN

ETHICALLY SOURCED COFFEE

On Top: 100% Arabica Beans

On Left Side:
Coffee brew guide: https://in.brewboardly.com/pin/318274659201847362/
https://in.brewboardly.com/pin/coffee-brewing-method-chart--207431985562143/

On right side bottom:
STORAGE
Proper storage is essential to maintaining your coffee’s freshness and flavor. Once opened, we recommend keeping your coffee in a cool, dark, dry place and sealed in an airtight container. Always reseal the bag after each use to preserve maximum freshness and aroma.

487 Tullane Street Oakland Ca 94619

Follow Us
www.velmiran.com
TikTok@velmiran
IG@getvelmiran

Target Market(s)

Coffee/ Cafe

Industry/Entity Type

Coffee

Font styles to use
Other font styles liked:
• Non‑Seasonal Sans

Requirements
Must have
• Clean, modern
Nice to have
• Elegant

```html
<!DOCTYPE html>
<html lang="en">
<head>
<meta charset="UTF-8">
<title>VELMIRAN – Panel 3 Front</title>
<link rel="stylesheet" href="https://fonts.googleapis.com/css2?family=Barlow+Condensed:wght@500;600;700&family=Libre+Caslon+Text:wght@700&display=swap">
<style>
  :root {
    --page: #ffffff;
    --frame: #222222;
    --ink: #1d1d1b;
    --panel: #f4f3f0;
    --trim-line: #29a9e0;
    --safe-line: #1f9a4a;
    --print-ink: #000000;
  }
  html, body {
    margin: 0;
    padding: 0;
    width: 775px;
    height: 1200px;
    overflow: hidden;
    background: var(--page);
  }
  .sheet {
    position: relative;
    width: 775px;
    height: 1200px;
    box-sizing: border-box;
    border: 1px solid var(--frame);
    background: var(--page);
  }
  .spec {
    position: absolute;
    left: 0;
    width: 100%;
    text-align: center;
    color: var(--ink);
    font-family: "Barlow Condensed", sans-serif;
    margin: 0;
    line-height: 1;
  }
  .spec-title {
    top: 56px;
    font-size: 53px;
    font-weight: 600;
    letter-spacing: 0.5px;
  }
  .spec-side {
    top: 104px;
    font-size: 21px;
    font-weight: 500;
  }
  .spec-size {
    top: 130px;
    font-size: 19px;
    font-weight: 700;
    letter-spacing: 0.3px;
  }
  .artboard {
    position: absolute;
    left: 0;
    top: 0;
  }
  .claim {
    position: absolute;
    left: 179px;
    top: 238px;
    margin: 0;
    font-family: "Libre Caslon Text", serif;
    font-weight: 700;
    font-size: 35px;
    line-height: 35px;
    letter-spacing: -1px;
    color: var(--print-ink);
  }
  .brand-name {
    font-family: "Libre Caslon Text", serif;
    font-weight: 700;
    fill: var(--print-ink);
  }
</style>
</head>
<body>
  <main class="sheet">
    <h1 class="spec spec-title">PANEL #3</h1>
    <p class="spec spec-side">Front</p>
    <p class="spec spec-size">5,4554” Width x 9,25” Height</p>

    <svg class="artboard" width="775" height="1200" viewBox="0 0 775 1200" aria-hidden="false">
      <rect class="bleed-panel" x="120" y="161" width="547" height="909" fill="var(--panel)"/>
      <rect class="trim-line" x="135" y="173" width="523" height="886" rx="25" ry="25" fill="none" stroke="var(--trim-line)" stroke-width="0.8"/>
      <rect class="safe-line" x="174" y="220.5" width="444" height="790.5" fill="none" stroke="var(--safe-line)" stroke-width="0.8"/>
      <text class="brand-name" transform="translate(281 1006) rotate(-90)" x="0" y="0" font-size="148" textLength="602" lengthAdjust="spacingAndGlyphs">VELMIRAN</text>
    </svg>

    <p class="claim">100%<br>ARABICA<br>BEAN</p>
  </main>
</body>
</html>
```